MD Trailcraft & Wildland Expo

I need a 1 page flyer for promotion of an upcoming sportsman and outdoor show(expo). would like the flyer to be able to be printed in B&W and color! show will include all things to do with the out doors, hunting fishing boating hiking atv camping rvs motorcycles. the event will have a kids zone, events games and activities for kids. there will be vendors showing the newest products. guest speakers and industry experts giving training and advice. this show will have something for everyone. food trucks and concessions. 200+ vendors. waterfould calling competition. deer/buck scoring casting competition for kids 3D Archery competitions

Target Market(s)

anyone event open to all ages!

Colors
ec1f27
000000
fbed22

Requirements
Must have
• date- september 1-2 2018
• location Penwick county fair 4817 millbrook rd east caldon MD 21638
• facebook - mdtrailcraftexpo
• email mdtrailcraftexpo@mailvento.com
• web www.mdtrailcraftexpo-demo.com
• vendor spaces still available! sign up now space going fast
Nice to have
• would like some thing that can be both printed in B&W and Color, and still have a great affect.
Should not have
• open to any suggestions

```html
<!DOCTYPE html>
<html lang="en">
<head>
<meta charset="utf-8">
<title>MD Trailcraft &amp; Wildland Expo – Flyer</title>
<link rel="stylesheet" href="https://fonts.googleapis.com/css2?family=Cinzel:wght@400;500&family=Lato:ital,wght@0,400;0,700;0,900;1,700;1,900&display=swap">
<style>
  :root {
    --red: #ec1f27;
    --red-deep: #b8141b;
    --black: #0b0b0b;
    --white: #ffffff;
    --ink: #111111;
    --gap-gray: #d9d9d9;
    --backdrop: #e2e2e2;
    --page-light: #ffffff;
    --page-shade: #dcdcdc;
  }
  * { margin: 0; padding: 0; box-sizing: border-box; }
  html, body { width: 1200px; height: 1200px; overflow: hidden; background: var(--backdrop); }
  .flyer {
    position: absolute; left: 160px; top: 30px;
    width: 981px; height: 1270px;
    transform: scale(0.8976); transform-origin: 0 0;
    background: linear-gradient(135deg, var(--page-light) 40%, var(--page-shade) 100%);
    overflow: hidden;
    font-family: "Lato", Arial, sans-serif;
  }
  .flyer__shapes { position: absolute; inset: 0; }
  .abs { position: absolute; white-space: nowrap; }
  .title {
    left: 494px; transform: translateX(-50%);
    font-family: "Cinzel", Georgia, serif; font-weight: 400; color: var(--red);
    font-size: 35px; line-height: 46px; text-align: center; letter-spacing: 0.5px;
  }
  .headline {
    left: 300px; top: 736px; font-weight: 900; font-size: 28.5px; line-height: 35px; color: var(--ink);
  }
  .checklist { font-size: 17px; color: var(--ink); }
  .checklist li { position: absolute; list-style: none; display: flex; gap: 8px; white-space: nowrap; }
  .checklist span::before { content: "✓"; color: var(--red); font-weight: 900; font-size: 13px; margin-right: 5px; }
  .more { left: 592px; top: 1012px; font-size: 27px; color: var(--ink); }
  .date { font-family: "Cinzel", Georgia, serif; color: var(--white); font-size: 58px; line-height: 64px; }
  .pitch { left: 26px; top: 1064px; font-family: "Cinzel", Georgia, serif; color: var(--white); font-size: 21px; line-height: 23px; }
  .attendance { left: 26px; top: 1130px; color: var(--white); font-style: italic; font-weight: 700; font-size: 16.5px; }
  .vendor { color: var(--red); font-weight: 900; font-style: italic; font-size: 29px; line-height: 35px; }
  .vendor--spread { display: flex; justify-content: space-between; }
  .footer-text { color: var(--white); font-size: 12.5px; line-height: 16px; }
</style>
</head>
<body>
<main class="flyer">
  <svg class="flyer__shapes" viewBox="0 0 981 1270" width="981" height="1270">
    <defs>
      <linearGradient id="redFade" x1="0" y1="0" x2="1" y2="0">
        <stop offset="0" stop-color="#ec1f27"/><stop offset="0.6" stop-color="#c4161d"/><stop offset="1" stop-color="#9e1016"/>
      </linearGradient>
      <linearGradient id="archeryTone" x1="0" y1="0" x2="0" y2="1">
        <stop offset="0" stop-color="#8a9a6a"/><stop offset="0.35" stop-color="#c9a97a"/><stop offset="1" stop-color="#d8b98c"/>
      </linearGradient>
      <radialGradient id="golfTone" cx="0.55" cy="0.45" r="0.6">
        <stop offset="0" stop-color="#f4f4f4"/><stop offset="0.35" stop-color="#e6e6e6"/><stop offset="0.6" stop-color="#7ea24a"/><stop offset="1" stop-color="#4f7a2c"/>
      </radialGradient>
      <linearGradient id="waterTone" x1="0" y1="0" x2="0" y2="1">
        <stop offset="0" stop-color="#a9c9e4"/><stop offset="0.35" stop-color="#d8ecf2"/><stop offset="0.7" stop-color="#4f9fc0"/><stop offset="1" stop-color="#2c86a8"/>
      </linearGradient>
    </defs>

    <polygon points="0,0 288,0 0,292" fill="url(#redFade)"/>
    <polygon points="686,0 981,0 981,297" fill="var(--black)"/>
    <polygon points="0,514 0,696 178,696" fill="var(--black)"/>
    <polygon points="981,514 981,700 796,700" fill="url(#redFade)"/>

    <polygon role="img" aria-label="Photo: archer drawing a bow toward a target on a sandy range"
             points="333,0 683,0 760,112 503,384 222,112" fill="url(#archeryTone)"/>
    <polygon role="img" aria-label="Photo: close-up of a golf ball on a tee over green grass"
             points="195,130 470,405 203,680 0,476 0,306" fill="url(#golfTone)"/>
    <polygon role="img" aria-label="Photo: rider on a jet ski spraying water across a lake"
             points="758,130 981,353 981,492 790,678 513,405" fill="url(#waterTone)"/>

    <rect x="0" y="700" width="981" height="24" fill="var(--gap-gray)" opacity="0.7"/>
    <polygon points="0,724 205,724 598,1174 0,1174" fill="url(#redFade)"/>
    <polygon points="0,1174 598,1174 656,1240 981,1240 981,1270 0,1270" fill="var(--black)"/>

    <g fill="var(--white)">
      <path d="M35 1188 a9 9 0 0 1 9 9 c0 7 -9 16 -9 16 s-9 -9 -9 -16 a9 9 0 0 1 9 -9z M35 1193 a4 4 0 1 0 0.01 0z" fill-rule="evenodd"/>
      <circle cx="32" cy="1240" r="6"/>
      <rect x="369" y="1195" width="24" height="17" rx="2"/>
      <path d="M371 1197 l10 8 l10 -8" stroke="var(--black)" stroke-width="2" fill="none"/>
    </g>
    <g fill="none" stroke="var(--white)" stroke-width="1.8">
      <circle cx="385" cy="1241" r="9"/>
      <ellipse cx="385" cy="1241" rx="4" ry="9"/>
      <line x1="376" y1="1241" x2="394" y2="1241"/>
    </g>
  </svg>

  <h1 class="abs title" style="top:598px">MD TRAILCRAFT &amp;<br>WILDLAND EXPO</h1>

  <p class="abs headline">Over 60,000 sqft of INDOOR and 30,000+ sqft<br>OUTDOOR products and services including:</p>

  <ul class="checklist">
    <li style="left:350px;top:837px"><span>Sports Equipment</span><span>Campers</span><span>Boats</span><span>RV’s</span><span>Tackle &amp; Bait</span></li>
    <li style="left:378px;top:867px"><span>Motorcycles</span><span>ATV’s</span><span>Trucks</span><span>Taxidermists</span><span>Outfitters</span></li>
    <li style="left:412px;top:898px"><span>Guns</span><span>Jet Skis</span><span>Charter Boats</span><span>Golf Resorts</span></li>
    <li style="left:446px;top:928px"><span>Knives</span><span>Archery</span><span>Trailers</span><span>Sporting Clubs</span></li>
    <li style="left:479px;top:959px"><span>Game Calls</span><span>Outdoor Magazines</span><span>Camp Grounds</span></li>
    <li style="left:513px;top:989px"><span>Camping Equipment</span><span>Hunting Supplies</span></li>
  </ul>
  <p class="abs more">and much more…</p>

  <p class="abs date" style="left:24px;top:906px">SEPTEMBER</p>
  <p class="abs date" style="left:56px;top:970px">1-2, 2018</p>

  <p class="abs pitch">SELL YOUR PRODUCTS AND SERVICES TO<br>THOUSANDS OF PEOPLE IN ONE WEEKEND!!</p>
  <p class="abs attendance">WE ARE EXPECTING 2 DAY ATTENDANCE TO TOP 15,000 PEOPLE!</p>

  <div class="abs vendor vendor--spread" style="left:578px;top:1082px;width:380px"><span>VENDOR</span><span>SPACES</span><span>STILL</span></div>
  <div class="abs vendor vendor--spread" style="left:606px;top:1117px;width:352px"><span>AVAILABLE!</span><span>SIGN</span><span>UP</span><span>NOW</span></div>
  <div class="abs vendor" style="left:638px;top:1152px">SPACE GOING FAST</div>

  <p class="abs footer-text" style="left:55px;top:1186px">Penwick county fair,<br>4817 millbrook rd east caldon MD 21638</p>
  <p class="abs footer-text" style="left:51px;top:1233px">mdtrailcraftexpo</p>
  <p class="abs footer-text" style="left:406px;top:1196px">mdtrailcraftexpo@mailvento.com</p>
  <p class="abs footer-text" style="left:406px;top:1233px">mdtrailcraftexpo-demo.com</p>
</main>
</body>
</html>
```